PSD Only - Wordpress Magazine Theme Design

We need a design for our new Premuim wordpress Magazine theme design based on our basic wire-frame. The theme will be used by people who run online magazine, news website or just blog in general.

The layout of homepage is showing recent posts in many way which is easy to user to customize the section of their homepage to show their post based on various categories.

2 Page design need (Homepage and Single Post)
Updates

Project Deadline Extended
Reason: want to get more designer and I am off for holiday a few days too. Better extend the time for designers as well as me also.

Target Market(s)

General Blogger who want a nice premium theme as well as other content based wesite.

Industry/Entity Type

Online

Font styles to use
Sans Serif

Requirements
Must have
• + Must have 2 page design based on Wireframing. Homepage (home.png) annd Single Post (Single.png)
• + Layout must be based on wireframe.
• + Width 1025px
• + 2 Navigation Menu in Header Must be in different style. When theme goes public, user can choose to have both or only 1 navigation or completely hide both of them.
• + 2 Featured Content Slider as you see in wire-frame. They must be in different style from each other.
• + Those recent news section is only about arrange post in defferent ways which only include post feature image, post title as well as post meta info.
• + Sidebar Widget Must be 300px (not include margin or padding) in order to be able for user to place ads with (300px of width) in sidebar widget)
• + Footer Widget Section should have a bit different colour in order to look different for main layout.
Nice to have
• + Drop down Menu
• + (Optional) Some custom Widget (Based on your imagination and creativity)

```html
<!DOCTYPE html>
<html lang="en">
<head>
<meta charset="utf-8">
<title>Kestrel Magazine — Home</title>
<link href="https://fonts.googleapis.com/css2?family=Open+Sans:wght@400;600;700;800&display=swap" rel="stylesheet">
<style>
:root{
  --blue:#2b8fd8;
  --blue-dark:#1f74b5;
  --blue-light:#b6d6f2;
  --bg:#e6e6e6;
  --panel:#ffffff;
  --text:#333333;
  --muted:#9a9a9a;
  --line:#e2e2e2;
  --red:#d6443a;
  --foot:#5c5c5c;
  --foot-dark:#474747;
  --foot-text:#d4d4d4;
}
*{box-sizing:border-box;margin:0;padding:0}
html,body{width:1200px;height:5156px;overflow:hidden}
body{background:var(--bg);font-family:"Open Sans",Arial,sans-serif;color:var(--text);font-size:13px;line-height:1.45;position:relative}
a{color:inherit;text-decoration:none}
.abs{position:absolute}
.panel{position:absolute;background:var(--panel);padding:16px;overflow:hidden}
.ph{display:block;border-radius:1px}
.sec-title{display:flex;align-items:center;gap:12px;color:var(--blue);font-weight:700;font-size:14px;text-transform:uppercase;margin-bottom:16px}
.sec-title::after{content:"";flex:1;height:8px;background:var(--blue-light)}
.title{font-weight:700;font-size:14px;line-height:1.3;color:#222}
.meta{font-size:11px;color:var(--muted);margin:4px 0}
.excerpt{font-size:12px;color:#666;line-height:1.5}
.more{color:var(--blue);font-size:12px;font-weight:600}
.more::after{content:" \2192"}
.show-more{text-align:center;font-size:12px;color:#777;border-top:1px solid var(--line);padding-top:8px;position:absolute;left:16px;right:16px;bottom:12px}
.dots{display:flex;gap:6px;justify-content:center}
.dots span{width:8px;height:8px;border-radius:50%;background:#ccc}
.dots span.on{background:var(--blue)}
/* header */
.topbar{left:40px;top:0;width:1120px;height:32px;background:var(--blue);color:#fff;display:flex;align-items:center;justify-content:space-between;padding:0 14px;font-size:11px}
.topbar nav{display:flex;gap:18px}
.topbar .soc{display:flex;gap:8px}
.topbar .soc i{width:14px;height:14px;background:#fff;opacity:.85;border-radius:2px;display:block}
.header{left:40px;top:32px;width:1120px;height:144px;background:var(--panel)}
.brand{position:absolute;left:24px;top:40px}
.brand b{font-size:34px;font-weight:800;color:var(--blue);letter-spacing:.5px}
.brand small{display:block;font-size:11px;color:var(--muted);margin-top:-2px}
.banner{position:absolute;left:560px;top:24px;width:528px;height:88px;background:linear-gradient(90deg,#f4d34a 0%,#f7e07a 30%,#f2b53a 75%,#2a8ad6 76%,#2a8ad6 100%)}
.mainnav{left:40px;top:176px;width:1120px;height:48px;background:var(--blue);display:flex;align-items:center;padding:0 16px;color:#fff;font-size:12px;font-weight:700}
.mainnav .home{width:18px;height:18px;margin-right:22px}
.mainnav a{margin-right:26px}
.search{margin-left:auto;display:flex}
.search span{width:170px;height:24px;background:#fff;color:#999;font-weight:400;font-size:11px;padding:4px 8px}
.search b{width:40px;height:24px;background:var(--blue-dark);display:block}
/* cards */
.row{display:flex;gap:18px}
.col{flex:1;min-width:0}
.item-s{display:flex;gap:12px;margin-bottom:16px}
.item-s .ph{flex:none}
.item-s .title{font-size:12px}
/* sidebar */
.recent .entry{margin-bottom:40px}
.recent .entry .title{color:var(--blue);margin-bottom:8px}
.recent .entry .body{display:flex;gap:14px}
.cat-list{list-style:none;font-size:13px}
.cat-list li{padding:4px 0 4px 14px;position:relative}
.cat-list li::before{content:"";position:absolute;left:0;top:12px;width:5px;height:5px;background:var(--text)}
.field{height:30px;border:1px solid #ddd;margin-bottom:10px;font-size:11px;color:#aaa;padding:6px 10px}
.btn{display:inline-block;background:var(--red);color:#fff;font-size:12px;font-weight:600;padding:6px 14px}
.squares{display:grid;grid-template-columns:repeat(6,36px);gap:8px}
.squares i{width:36px;height:36px;display:block;border-radius:2px}
/* footer */
.footer{left:0;top:4784px;width:1200px;height:320px;background:var(--foot);color:var(--foot-text);padding:28px 40px;display:flex;gap:40px}
.footer h4{color:#fff;font-size:14px;font-weight:700;text-transform:uppercase;margin-bottom:14px}
.footer .fcol{flex:1}
.footer ul{list-style:none;font-size:12px;line-height:1.9}
.footer .field{background:#fff;border:none}
.bottom{left:0;top:5104px;width:1200px;height:52px;background:var(--foot-dark);color:var(--foot-text);font-size:11px;display:flex;align-items:center;padding:0 40px}
.totop{margin-left:auto;width:32px;height:32px;background:#777;display:flex;align-items:center;justify-content:center}
</style>
</head>
<body>

<div class="abs topbar">
  <nav><a>Home</a><a>About Us</a><a>Contact Us</a><a>Resources</a></nav>
  <div class="soc"><i></i><i></i><i></i><i></i><i></i><i></i><i></i></div>
</div>

<header class="abs header">
  <div class="brand"><b>KESTREL MAGAZINE</b><small>Fresh stories, every single day</small></div>
  <div class="banner ph" role="img" aria-label="Advertising banner: Shade Hub sunglasses sale"></div>
</header>

<nav class="abs mainnav">
  <svg class="home" viewBox="0 0 18 18"><path d="M2 9 9 2l7 7h-2v7h-4v-5H8v5H4V9z" fill="#fff"/></svg>
  <a>ABOUT US</a><a>CONTACT US</a><a>RESOURCE</a>
  <div class="search"><span>Search...</span><b></b></div>
</nav>

<div class="abs ph" style="left:40px;top:256px;width:1120px;height:368px;background:linear-gradient(160deg,#c9d3dc 0%,#8f9cab 40%,#e8ecf0 70%,#b5c0cb 100%)" role="img" aria-label="Featured slide: skier racing downhill in the snow"></div>

<!-- MAIN COLUMN -->
<section class="panel" style="left:40px;top:640px;width:608px;height:520px">
  <div class="ph" style="height:384px;background:linear-gradient(180deg,#7fb6e6 0%,#cfe2f3 45%,#5d7a93 55%,#d8c39a 80%,#b89f72 100%)" role="img" aria-label="Featured slide: quiet beach with hills across the bay"></div>
  <div class="row" style="gap:8px;margin-top:16px">
    <div class="col ph" style="height:64px;background:#8fa9c2" role="img" aria-label="Thumbnail: coastline"></div>
    <div class="col ph" style="height:64px;background:#6f8fae" role="img" aria-label="Thumbnail: mountain view"></div>
    <div class="col ph" style="height:64px;background:#a08b6e" role="img" aria-label="Thumbnail: desert road"></div>
    <div class="col ph" style="height:64px;background:#7d9a6a" role="img" aria-label="Thumbnail: forest"></div>
    <div class="col ph" style="height:64px;background:#b4c4d3" role="img" aria-label="Thumbnail: snow field"></div>
    <div class="col ph" style="height:64px;background:#56708c" role="img" aria-label="Thumbnail: harbour"></div>
    <div class="col ph" style="height:64px;background:#9aa7b3" role="img" aria-label="Thumbnail: city skyline"></div>
  </div>
</section>

<section class="panel" style="left:40px;top:1176px;width:608px;height:376px">
  <h3 class="sec-title">Latest News</h3>
  <div class="row">
    <article class="col"><div class="ph" style="height:120px;background:#6b5a4e" role="img" aria-label="Photo: man speaking at an event"></div>
      <div class="title" style="margin-top:8px;font-size:12px">Itaque earum rerum hic tenetur a sapiente</div><div class="meta">Posted by admin</div><p class="excerpt">Sed ut perspiciatis unde omnis iste natus error sit.</p></article>
    <article class="col"><div class="ph" style="height:120px;background:#3f5568" role="img" aria-label="Photo: evening city street"></div>
      <div class="title" style="margin-top:8px;font-size:12px">Temporibus autem quibusdam et aut</div><div class="meta">Posted by admin</div><p class="excerpt">Nemo enim ipsam voluptatem quia voluptas sit.</p></article>
    <article class="col"><div class="ph" style="height:120px;background:#8b6f5a" role="img" aria-label="Photo: group portrait outdoors"></div>
      <div class="title" style="margin-top:8px;font-size:12px">Nemo enim ipsam voluptatem quia</div><div class="meta">Posted by admin</div><p class="excerpt">Neque porro quisquam est qui dolorem ipsum.</p></article>
  </div>
  <div class="dots" style="margin-top:16px"><span class="on"></span><span></span></div>
</section>

<section class="panel" style="left:40px;top:1568px;width:608px;height:512px">
  <h3 class="sec-title">Latest News</h3>
  <div class="row" style="gap:24px">
    <article class="col"><div class="ph" style="height:168px;background:linear-gradient(180deg,#3b6fb0,#1f3f73)" role="img" aria-label="Photo: football player in a blue kit"></div>
      <div class="title" style="margin-top:10px">Nemo enim ipsam voluptatem quia voluptas sit</div><div class="meta">September 7, 2014</div>
      <p class="excerpt">Sed ut perspiciatis unde omnis iste natus error sit voluptatem accusantium doloremque laudantium, totam rem aperiam eaque ipsa quae ab illo inventore.</p><a class="more">Read more</a></article>
    <article class="col"><div class="ph" style="height:168px;background:linear-gradient(180deg,#9aa8b5,#5d6d7c)" role="img" aria-label="Photo: people walking in a park"></div>
      <div class="title" style="margin-top:10px">Labore et dolore magnam aliquam quaerat voluptatem</div><div class="meta">September 7, 2014</div>
      <p class="excerpt">At vero eos et accusamus et iusto odio dignissimos ducimus qui blanditiis praesentium voluptatum deleniti atque corrupti quos dolores.</p><a class="more">Read more</a></article>
  </div>
  <div class="show-more">Show More</div>
</section>

<section class="panel" style="left:40px;top:2096px;width:608px;height:448px">
  <h3 class="sec-title">Latest News</h3>
  <div class="row" style="gap:24px">
    <article class="col"><div class="ph" style="height:128px;background:linear-gradient(135deg,#c9a35e,#7d5a2e)" role="img" aria-label="Photo: plate of food on a table"></div>
      <div class="title" style="margin-top:10px">Saepe eveniet ut et voluptates repudiandae sint</div><div class="meta">September 7, 2014</div>
      <p class="excerpt">Quis autem vel eum iure reprehenderit qui in ea voluptate velit esse quam nihil molestiae consequatur.</p><a class="more">Read more</a></article>
    <div class="col">
      <div class="item-s"><div class="ph" style="width:60px;height:44px;background:#a4835c" role="img" aria-label="Photo: bakery goods"></div><div><div class="title">Dolore magnam aliquam quaerat</div><div class="meta">June 2014</div></div></div>
      <div class="item-s"><div class="ph" style="width:60px;height:44px;background:#6b8a5a" role="img" aria-label="Photo: garden vegetables"></div><div><div class="title">Vel illum qui dolorem eum fugiat</div><div class="meta">June 2014</div></div></div>
      <div class="item-s"><div class="ph" style="width:60px;height:44px;background:#b88b60" role="img" aria-label="Photo: coffee cup"></div><div><div class="title">Rerum necessitatibus saepe</div><div class="meta">June 2014</div></div></div>
      <div class="item-s"><div class="ph" style="width:60px;height:44px;background:#7a6050" role="img" aria-label="Photo: kitchen table"></div><div><div class="title">Natus error sit voluptatem</div><div class="meta">June 2014</div></div></div>
    </div>
  </div>
  <div class="show-more">Show More</div>
</section>

<section class="panel" style="left:40px;top:2560px;width:608px;height:400px">
  <h3 class="sec-title">Latest News</h3>
  <div class="row" style="gap:24px">
    <div class="col">
      <div class="item-s"><div class="ph" style="width:56px;height:42px;background:#8c6b52" role="img" aria-label="Photo: street market"></div><div class="title">Quis autem vel eum iure reprehenderit</div></div>
      <div class="item-s"><div class="ph" style="width:56px;height:42px;background:#5f7f99" role="img" aria-label="Photo: lake view"></div><div class="title">Temporibus autem quibusdam et aut</div></div>
      <div class="item-s"><div class="ph" style="width:56px;height:42px;background:#a6917a" role="img" aria-label="Photo: old building"></div><div class="title">Sunt in culpa qui officia deserunt</div></div>
      <div class="item-s"><div class="ph" style="width:56px;height:42px;background:#6e6259" role="img" aria-label="Photo: night traffic"></div><div class="title">Itaque earum rerum hic tenetur</div></div>
    </div>
    <div class="col">
      <div class="item-s"><div class="ph" style="width:56px;height:42px;background:#9a7b60" role="img" aria-label="Photo: library shelves"></div><div class="title">Molestiae non recusandae itaque</div></div>
      <div class="item-s"><div class="ph" style="width:56px;height:42px;background:#7c90a3" role="img" aria-label="Photo: harbour boats"></div><div class="title">Temporibus autem quibusdam et aut</div></div>
      <div class="item-s"><div class="ph" style="width:56px;height:42px;background:#b59a77" role="img" aria-label="Photo: dessert plate"></div><div class="title">Eveniet ut et voluptates repudiandae</div></div>
      <div class="item-s"><div class="ph" style="width:56px;height:42px;background:#576b52" role="img" aria-label="Photo: hiking trail"></div><div class="title">Nam libero tempore cum soluta</div></div>
    </div>
  </div>
  <div class="show-more">SHOW MORE</div>
</section>

<section class="panel" style="left:40px;top:2976px;width:608px;height:368px">
  <h3 class="sec-title">Latest News</h3>
  <article class="row" style="margin-bottom:24px"><div class="ph" style="width:180px;height:112px;flex:none;background:linear-gradient(135deg,#c9a46a,#8a5b34)" role="img" aria-label="Photo: food stall"></div>
    <div><div class="title">Similique sunt in culpa qui officia deserunt mollitia animi</div><p class="excerpt" style="margin-top:6px">Et harum quidem rerum facilis est et expedita distinctio nam libero tempore cum soluta. <a class="more">Read more</a></p><div class="meta">By admin on June 2014</div></div></article>
  <article class="row"><div class="ph" style="width:180px;height:112px;flex:none;background:linear-gradient(135deg,#8a6e5a,#4b3a30)" role="img" aria-label="Photo: people at a conference"></div>
    <div><div class="title">Exercitation ullamco laboris nisi ut aliquip ex ea commodo consequat</div><p class="excerpt" style="margin-top:6px">Duis aute irure dolor in reprehenderit in voluptate velit esse cillum dolore fugiat. <a class="more">Read more</a></p><div class="meta">By admin on June 2014</div></div></article>
</section>

<section class="panel" style="left:40px;top:3392px;width:608px;height:1328px">
  <h3 class="sec-title">Latest News</h3>
  <article style="margin-bottom:40px"><div class="ph" style="height:240px;background:linear-gradient(135deg,#cfd6dc,#7f97ad 50%,#b3473f)" role="img" aria-label="Photo: crowd wearing face masks"></div>
    <div class="title" style="margin-top:12px;font-size:15px">Temporibus autem quibusdam et aut officiis debitis aut rerum necessitatibus saepe eveniet</div><div class="meta">Posted by admin on 30th March, 2014</div>
    <p class="excerpt">Nam libero tempore, cum soluta nobis est eligendi optio cumque nihil impedit quo minus id quod maxime placeat facere possimus, omnis voluptas assumenda est, omnis dolor repellendus. <a class="more">Read more</a></p></article>
  <article style="margin-bottom:40px"><div class="ph" style="height:240px;background:linear-gradient(135deg,#9cc3e6,#f0d24a 60%,#8ab6de)" role="img" aria-label="Photo: smiling person against a bright sky"></div>
    <div class="title" style="margin-top:12px;font-size:15px">Ut enim ad minima veniam, quis nostrum exercitationem ullam corporis suscipit laboriosam</div><div class="meta">Posted by admin on 19th March, 2014</div>
    <p class="excerpt">Quis autem vel eum iure reprehenderit qui in ea voluptate velit esse quam nihil molestiae consequatur, vel illum qui dolorem eum fugiat quo voluptas nulla pariatur. <a class="more">Read more</a></p></article>
  <article><div class="ph" style="height:240px;background:linear-gradient(180deg,#7fa0c0,#6f8c55 55%,#b8493a)" role="img" aria-label="Photo: train crossing a green valley"></div>
    <div class="title" style="margin-top:12px;font-size:15px">Temporibus autem quibusdam et aut officiis debitis aut rerum necessitatibus saepe eveniet</div><div class="meta">Posted by admin on 24th Dec, 2014</div>
    <p class="excerpt">Nam libero tempore, cum soluta nobis est eligendi optio cumque nihil impedit quo minus id quod maxime placeat facere possimus, omnis voluptas assumenda est. <a class="more">Read more</a></p></article>
</section>

<nav class="abs" style="left:40px;top:4736px;display:flex;gap:6px;font-size:12px">
  <span style="background:var(--blue);color:#fff;padding:4px 10px">1</span>
  <span style="background:#fff;padding:4px 10px">2</span>
  <span style="background:#fff;padding:4px 10px">Next</span>
</nav>

<!-- SIDEBAR -->
<aside class="panel recent" style="left:680px;top:632px;width:480px;height:856px">
  <h3 class="sec-title">Recent Posts</h3>
  <div class="entry"><div class="title">Quis autem vel eum iure</div><div class="body"><div class="ph" style="width:150px;height:108px;flex:none;background:#4f7fb0" role="img" aria-label="Photo: sea view"></div><div><div class="meta" style="margin-top:0">March 2014</div><p class="excerpt">Neque porro quisquam est, qui dolorem ipsum quia dolor sit amet, consectetur, adipisci velit. <a class="more">Read more</a></p></div></div></div>
  <div class="entry"><div class="title">Qui dolorem eum fugiat quo voluptas</div><div class="body"><div class="ph" style="width:150px;height:108px;flex:none;background:#6a8fb5" role="img" aria-label="Photo: city river"></div><div><div class="meta" style="margin-top:0">March 2014</div><p class="excerpt">Neque porro quisquam est, qui dolorem ipsum quia dolor sit amet, consectetur, adipisci velit. <a class="more">Read more</a></p></div></div></div>
  <div class="entry"><div class="title">Saepe eveniet ut et voluptates</div><div class="body"><div class="ph" style="width:150px;height:108px;flex:none;background:#5c7a55" role="img" aria-label="Photo: countryside road"></div><div><div class="meta" style="margin-top:0">March 2014</div><p class="excerpt">Neque porro quisquam est, qui dolorem ipsum quia dolor sit amet, consectetur, adipisci velit. <a class="more">Read more</a></p></div></div></div>
  <div class="entry"><div class="title">Omnis voluptas assumenda est</div><div class="body"><div class="ph" style="width:150px;height:108px;flex:none;background:#3c3f44" role="img" aria-label="Photo: smartphone on a desk"></div><div><div class="meta" style="margin-top:0">March 2014</div><p class="excerpt">Neque porro quisquam est, qui dolorem ipsum quia dolor sit amet, consectetur, adipisci velit. <a class="more">Read more</a></p></div></div></div>
</aside>

<aside class="panel" style="left:672px;top:1512px;width:184px;height:240px">
  <h3 class="sec-title">Category</h3>
  <ul class="cat-list"><li>Category 1</li><li>Category 2</li><li>Category 3</li><li>Category 4</li></ul>
</aside>

<aside class="panel" style="left:872px;top:1512px;width:288px;height:368px">
  <h3 class="sec-title">Most Popular Posts</h3>
  <div class="item-s"><div class="ph" style="width:64px;height:46px;background:#6d5a4c" role="img" aria-label="Photo: film scene"></div><div><div class="title">New movie star plans drama part</div><div class="meta">March 2014</div></div></div>
  <div class="item-s"><div class="ph" style="width:64px;height:46px;background:#5b87ad" role="img" aria-label="Photo: island beach"></div><div><div class="title">Quiet island holiday tips for this year</div><div class="meta">March 2014</div></div></div>
  <div class="item-s"><div class="ph" style="width:64px;height:46px;background:#8d7a66" role="img" aria-label="Photo: stage show"></div><div><div class="title">Review: Weekend stage show 2014</div><div class="meta">March 2014</div></div></div>
  <div class="item-s"><div class="ph" style="width:64px;height:46px;background:#4f5f70" role="img" aria-label="Photo: studio lights"></div><div><div class="title">New studio brings strong tale to screen</div><div class="meta">March 2014</div></div></div>
</aside>

<aside class="panel" style="left:672px;top:1776px;width:184px;height:664px">
  <h3 class="sec-title">Advertising</h3>
  <div class="ph" style="height:600px;background:linear-gradient(180deg,#4a6e8e,#29a0d6 45%,#1b5c8a 100%)" role="img" aria-label="Advertisement: limited edition book promotion"></div>
</aside>

<aside class="panel" style="left:872px;top:1912px;width:288px;height:216px">
  <h3 class="sec-title">Login</h3>
  <div class="field">Username</div>
  <div class="field">Password</div>
  <div style="display:flex;align-items:center;gap:14px;font-size:11px;color:#777"><span class="btn">Log in</span><span>☐ Remember Me</span></div>
</aside>

<aside class="panel" style="left:872px;top:2152px;width:288px;height:184px">
  <h3 class="sec-title">Follow Us</h3>
  <div class="squares">
    <i style="background:#3b5998"></i><i style="background:#29a9e1"></i><i style="background:#dd4b39"></i><i style="background:#f48b1f"></i><i style="background:#cb2027"></i><i style="background:#0e76a8"></i>
    <i style="background:#2d7bbf"></i><i style="background:#e14e4e"></i><i style="background:#f59f1b"></i><i style="background:#3aa0d8"></i><i style="background:#6d8fc7"></i><i style="background:#e04a6a"></i>
  </div>
</aside>

<aside class="panel" style="left:872px;top:2352px;width:288px;height:368px">
  <h3 class="sec-title">Community</h3>
  <div style="border:1px solid var(--line);padding:10px">
    <div style="display:flex;gap:10px;align-items:center"><div class="ph" style="width:40px;height:40px;background:var(--blue)" role="img" aria-label="Page avatar"></div><div><div class="title" style="font-size:12px;color:var(--blue)">Kestrel Magazine</div><span style="font-size:10px;border:1px solid #ccc;padding:0 6px">Join</span></div></div>
    <div style="font-size:10px;color:#777;margin:8px 0">1,240 readers follow Kestrel Magazine</div>
    <div style="display:grid;grid-template-columns:repeat(5,1fr);gap:6px">
      <i class="ph" style="height:40px;background:#8a7a6c" role="img" aria-label="Reader avatar"></i><i class="ph" style="height:40px;background:#6b7d8f" role="img" aria-label="Reader avatar"></i><i class="ph" style="height:40px;background:#a38d72" role="img" aria-label="Reader avatar"></i><i class="ph" style="height:40px;background:#5a6a5a" role="img" aria-label="Reader avatar"></i><i class="ph" style="height:40px;background:#907060" role="img" aria-label="Reader avatar"></i>
      <i class="ph" style="height:40px;background:#7f6a5e" role="img" aria-label="Reader avatar"></i><i class="ph" style="height:40px;background:#9aa5b0" role="img" aria-label="Reader avatar"></i><i class="ph" style="height:40px;background:#6f5a4a" role="img" aria-label="Reader avatar"></i><i class="ph" style="height:40px;background:#8c9a7c" role="img" aria-label="Reader avatar"></i><i class="ph" style="height:40px;background:#a07e66" role="img" aria-label="Reader avatar"></i>
    </div>
  </div>
</aside>

<aside class="panel" style="left:672px;top:2456px;width:184px;height:432px">
  <div style="display:flex;justify-content:space-between;align-items:center;border-bottom:1px solid var(--line);padding-bottom:8px;margin-bottom:12px"><b style="font-size:13px">Updates</b><span style="font-size:10px;border:1px solid #ccc;padding:1px 6px">Follow</span></div>
  <div class="item-s"><i class="ph" style="width:32px;height:32px;background:var(--blue)" role="img" aria-label="Account avatar"></i><div style="font-size:11px"><b>Kestrel Mag</b><br>New issue is live, read the latest stories now.</div></div>
  <div class="item-s"><i class="ph" style="width:32px;height:32px;background:#6a7f90" role="img" aria-label="Account avatar"></i><div style="font-size:11px"><b>Reader Desk</b><br>Great weekend guide, thanks for the tips.</div></div>
  <div class="item-s"><i class="ph" style="width:32px;height:32px;background:var(--blue)" role="img" aria-label="Account avatar"></i><div style="font-size:11px"><b>Kestrel Mag</b><br>Saepe eveniet ut et voluptates repudiandae sint.</div></div>
  <div style="border-top:1px solid var(--line);padding-top:8px;font-size:11px;color:#888">Write to the editors</div>
</aside>

<aside class="panel" style="left:872px;top:2744px;width:288px;height:216px">
  <h3 class="sec-title">Video</h3>
  <div class="ph" style="height:148px;background:linear-gradient(135deg,#7a8a6a,#4e5c66)" role="img" aria-label="Video: people gathered outdoors"></div>
</aside>

<!-- FOOTER -->
<footer class="abs footer">
  <div class="fcol"><h4>About Us</h4><p style="font-size:12px;line-height:1.6">Nam libero tempore, cum soluta nobis est eligendi optio cumque nihil impedit quo minus id quod maxime placeat facere possimus, omnis voluptas assumenda est, omnis dolor repellendus. Temporibus autem quibusdam et aut officiis debitis aut rerum necessitatibus saepe eveniet ut et voluptates repudiandae sint.</p></div>
  <div class="fcol"><h4>Link</h4><ul><li>World</li><li>Politics</li><li>Entertainment</li><li>Culture</li><li>Fashion</li><li>Lifestyle</li><li>Travel</li></ul></div>
  <div class="fcol"><h4>Contact Us</h4><div class="field">Name</div><div class="field">Email</div><div class="field" style="height:80px">Message</div><span class="btn" style="float:right">Submit</span></div>
  <div class="fcol"><h4>Follow Us</h4><div style="display:flex;gap:8px"><i style="width:24px;height:24px;background:#7a7a7a;display:block"></i><i style="width:24px;height:24px;background:#7a7a7a;display:block"></i><i style="width:24px;height:24px;background:#7a7a7a;display:block"></i><i style="width:24px;height:24px;background:#7a7a7a;display:block"></i><i style="width:24px;height:24px;background:#7a7a7a;display:block"></i><i style="width:24px;height:24px;background:#7a7a7a;display:block"></i></div></div>
</footer>
<div class="abs bottom"><span>© Copyright Kestrel Magazine 2014</span>
  <span class="totop"><svg width="14" height="14" viewBox="0 0 14 14"><path d="M7 2 2 8h3v4h4V8h3z" fill="#fff"/></svg></span></div>

</body>
</html>
```